Mental Health care Company in Washington DC

We are a new mental health care services provider in Washington DC. Please look at these sites.
https://marlowbrookpartners.com
https://www.quillstoneinc.com
https://velmarsh-kt.org/
https://www.trivanqx.com
https://www.thelanternofqz.com

```html
<!DOCTYPE html>
<html lang="en">
<head>
<meta charset="utf-8">
<title>Noren Health Services – Mental Health Care in Washington DC</title>
<link rel="stylesheet" href="https://fonts.googleapis.com/css2?family=Gilda+Display&family=Inter:wght@400;500;600;700&display=swap">
<style>
:root{
  --blue:#2e86cf;
  --blue-dark:#1f6fb3;
  --navy:#0f3350;
  --ink:#1d2b3a;
  --body:#4c5866;
  --tint:#e8f4fc;
  --tint-2:#dcebf8;
  --card:#ffffff;
  --line:#dfe6ec;
  --orange:#e8a86a;
  --plus:#c8e0f4;
}
*{box-sizing:border-box;margin:0;padding:0}
html,body{width:1200px;height:4166px;overflow:hidden}
body{font-family:"Inter",sans-serif;color:var(--ink);background:#fff;position:relative}
.serif{font-family:"Gilda Display",serif;font-weight:400}
section,header,footer{position:relative;width:1200px;overflow:hidden}
.abs{position:absolute}
.plus{position:absolute;width:70px;height:70px}
.plus::before,.plus::after{content:"";position:absolute;background:var(--plus);border-radius:12px}
.plus::before{left:24px;top:0;width:22px;height:70px}
.plus::after{top:24px;left:0;width:70px;height:22px}
.btn{position:absolute;display:flex;align-items:center;justify-content:center;font-size:13px;font-weight:500;border-radius:3px}
.btn-primary{background:var(--blue);color:#fff}
.btn-outline{border:1.5px solid var(--orange);color:var(--ink);background:#fff}
.btn-ghost{border:1.5px solid var(--line);background:#fff;color:var(--ink);box-shadow:0 2px 6px rgba(0,0,0,.06)}
.photo{position:absolute;border-radius:10px}
.ticks{list-style:none;font-size:12px;font-style:italic;color:var(--ink);line-height:22px}
.ticks li::before{content:"✓ ";font-style:normal}
.eyebrow{font-size:12px;font-weight:600;letter-spacing:1.2px;color:var(--blue);text-transform:uppercase}

/* header */
.site-header{height:81px;background:#fff}
.brand{position:absolute;display:flex;align-items:center;gap:10px}
.brand-dot{width:14px;height:14px;border-radius:50%;background:var(--blue)}
.brand-name{font-family:"Inter",sans-serif;font-weight:600;color:var(--navy);font-size:22px;line-height:1;white-space:nowrap}
.help{left:666px;top:28px;font-size:11px;line-height:14px;color:var(--ink)}
.header-divider{left:864px;top:25px;width:1px;height:34px;background:var(--line)}
.header-phone{left:892px;top:28px;display:flex;align-items:center;gap:12px;font-weight:600;font-size:18px;color:var(--ink)}
.icon-ring{width:28px;height:28px;border-radius:50%;border:1.5px solid var(--ink);display:flex;align-items:center;justify-content:center}

/* hero */
.hero{height:448px;background:var(--tint)}
.hero h1{position:absolute;left:137px;top:118px;font-size:38px;line-height:44px;color:var(--ink)}
.hero p{position:absolute;left:137px;top:224px;font-size:12.5px;line-height:22px;color:var(--body)}

/* specialized */
.spec{height:441px}
.section-title{position:absolute;font-size:30px;color:var(--ink)}
.section-sub{position:absolute;font-size:12px;color:var(--body)}
.cond{position:absolute;top:178px;width:210px;height:153px;background:#fff;border-radius:4px;box-shadow:0 4px 14px rgba(20,50,80,.1);display:flex;flex-direction:column;align-items:center;justify-content:center;gap:14px}
.cond .ico{width:52px;height:52px;border-radius:50%;border:2px solid var(--navy);background:var(--tint)}
.cond span{font-family:"Gilda Display",serif;font-size:17px;color:var(--ink)}
.cond.active{background:var(--blue)}
.cond.active span{color:#fff}
.cond.active .ico{border-color:#fff;background:transparent}

/* insurance */
.insurance{height:343px;background:var(--tint)}
.insurer{position:absolute;top:176px;width:165px;height:67px;background:#fff;border-radius:4px;box-shadow:0 3px 10px rgba(20,50,80,.08);display:flex;align-items:center;justify-content:center;font-weight:600;font-size:16px;color:var(--navy)}

/* about */
.about{height:490px}
.about-back{left:137px;top:90px;width:475px;height:370px;background:var(--tint-2);border-radius:14px}
.about p{font-size:12px;line-height:21px;color:var(--body)}

/* values */
.values{height:361px}
.value{position:absolute;top:134px;width:210px;height:130px;background:var(--tint);border-radius:6px;display:flex;align-items:flex-end;justify-content:center;padding-bottom:26px;text-align:center;font-family:"Gilda Display",serif;font-size:16px;line-height:22px;color:var(--ink)}
.value-icon{position:absolute;top:97px;width:72px;height:72px;border-radius:50%;background:#fff;box-shadow:0 3px 10px rgba(20,50,80,.12);display:flex;align-items:center;justify-content:center}
.value-icon i{width:40px;height:40px;border-radius:50%;border:2px solid var(--navy);display:block}

/* support */
.support{height:499px;background:var(--tint)}
.trust{left:487px;top:298px;width:138px;height:138px;border-radius:50%;background:var(--blue);border:5px solid #fff;color:#fff;display:flex;flex-direction:column;align-items:center;justify-content:center;text-align:center;font-family:"Gilda Display",serif;font-size:13px;line-height:17px;gap:6px}

/* facilities */
.facilities{height:474px}
.facility{position:absolute;top:199px;width:210px;height:218px;background:#fff;border-radius:4px;box-shadow:0 4px 14px rgba(20,50,80,.1);padding:22px 18px 22px 22px}
.facility .ico{width:52px;height:52px;border-radius:50%;background:var(--tint);display:flex;align-items:center;justify-content:center;margin-bottom:18px}
.facility .ico i{width:26px;height:26px;border:2px solid var(--blue-dark);border-radius:6px;display:block}
.facility h3{font-family:"Gilda Display",serif;font-weight:400;font-size:14.5px;margin-bottom:10px;white-space:nowrap}
.facility ul{list-style:none;font-size:10.5px;line-height:18px;color:var(--body)}
.facility li::before{content:"• "}

/* insights */
.insights{height:615px}
.post{position:absolute;top:123px;width:291px;height:370px;background:#fff;border-radius:4px;box-shadow:0 4px 14px rgba(20,50,80,.1);padding:14px}
.post .thumb{height:175px;border-radius:4px}
.post .date{font-size:12px;font-weight:500;margin:22px 8px 6px}
.post h3{font-family:"Gilda Display",serif;font-weight:400;font-size:13.5px;margin:0 8px 12px;white-space:nowrap}
.post ul,.post ol{font-size:11px;line-height:18px;color:var(--body);margin:0 8px 0 20px}
.post ul{list-style:disc}
.post a{display:block;margin:26px 8px 0;font-size:11px;color:var(--blue);text-decoration:underline}
.post a.muted{color:#9aa6b2}

/* footer */
.site-footer{height:414px;background:var(--navy);color:#fff}
.site-footer .brand-name{color:#fff;font-size:24px}
.f-tag{left:170px;top:130px;font-size:11px;line-height:18px;color:#c5d3df}
.f-col{position:absolute;top:84px}
.f-col h4{font-size:12px;font-weight:500;color:var(--blue);margin-bottom:22px;letter-spacing:.3px}
.f-col li{list-style:none;font-size:11px;color:#dbe5ee;margin-bottom:15px}
.contact-row{display:flex;align-items:center;gap:14px;font-size:11px;color:#dbe5ee;margin-bottom:16px}
.contact-dot{width:30px;height:30px;border-radius:50%;background:var(--blue);display:flex;align-items:center;justify-content:center}
.copyright{left:0;right:0;top:386px;text-align:center;font-size:12px;color:#b8c7d4}
.footer-rule{left:137px;width:926px;top:368px;height:1px;background:rgba(255,255,255,.12)}
</style>
</head>
<body>

<header class="site-header">
  <div class="brand" style="left:137px;top:30px">
    <span class="brand-dot"></span>
    <span class="brand-name">Noren Health Services</span>
  </div>
  <div class="abs help">Need Help?<br>Call Us 24/7 At Any Emergency</div>
  <div class="abs header-divider"></div>
  <div class="abs header-phone">
    <span class="icon-ring"><svg width="14" height="14" viewBox="0 0 24 24" fill="none" stroke="#1d2b3a" stroke-width="2"><path d="M5 3h4l2 5-3 2a11 11 0 0 0 6 6l2-3 5 2v4a2 2 0 0 1-2 2A18 18 0 0 1 3 5a2 2 0 0 1 2-2z"/></svg></span>
    (555) 014-2287
  </div>
</header>

<section class="hero">
  <span class="plus" style="left:30px;top:350px"></span>
  <span class="plus" style="left:1106px;top:30px"></span>
  <h1 class="serif">Healing Starts Here – For You,<br>Your Family, Our Community</h1>
  <p>Compassionate therapy, psychiatry, and addiction treatment – tailored to you.<br>Safe, inclusive, and accepting new clients</p>
  <span class="btn btn-primary" style="left:142px;top:297px;width:159px;height:34px">Start Healing Today</span>
  <span class="btn btn-outline" style="left:315px;top:297px;width:159px;height:34px">24/7 Crisis Support</span>
  <div class="photo" role="img" aria-label="Photo of a client talking with a therapist in a calm room" style="left:692px;top:35px;width:392px;height:369px;background:linear-gradient(135deg,#8a7262,#c9b9a7 55%,#6b6a6c)"></div>
</section>

<section class="spec">
  <h2 class="section-title serif" style="left:137px;top:80px">Find Specialized Care</h2>
  <p class="section-sub" style="left:137px;top:125px">Connect with 500+ Trusted Mental Health Providers</p>
  <span class="btn btn-ghost" style="left:943px;top:95px;width:141px;height:40px">View All Conditions</span>
  <div class="cond" style="left:137px"><i class="ico" role="img" aria-label="Depression icon"></i><span>Depression</span></div>
  <div class="cond active" style="left:373px"><i class="ico" role="img" aria-label="PTSD icon"></i><span>PTSD</span></div>
  <div class="cond" style="left:608px"><i class="ico" role="img" aria-label="Bipolar disorder icon"></i><span>Bi Polar Disorder</span></div>
  <div class="cond" style="left:843px"><i class="ico" role="img" aria-label="Anxiety icon"></i><span>Anxiety</span></div>
</section>

<section class="insurance">
  <span class="plus" style="left:1086px;top:52px"></span>
  <span class="plus" style="left:44px;top:250px"></span>
  <h2 class="section-title serif" style="left:0;right:0;text-align:center;top:64px">We Work With Your Insurance</h2>
  <p class="section-sub" style="left:0;right:0;text-align:center;top:103px;font-size:11.5px">Maximizing your benefits so you can focus on healing.</p>
  <div class="insurer" style="left:231px">Halvera</div>
  <div class="insurer" style="left:422px">Brightfield Mutual</div>
  <div class="insurer" style="left:613px">Corvane</div>
  <div class="insurer" style="left:804px">Westmere Care</div>
</section>

<section class="about">
  <div class="abs about-back"></div>
  <div class="photo" role="img" aria-label="Photo of the care team gathered around a table in a bright office" style="left:149px;top:86px;width:462px;height:357px;background:linear-gradient(135deg,#e7e6e2,#b9a690 50%,#6f6258)"></div>
  <div class="abs" style="left:653px;top:88px;width:400px">
    <div class="eyebrow">About Us</div>
    <h2 class="serif" style="font-size:28px;margin:10px 0 14px">Why Choose Noren Health?</h2>
    <p>Evidence-based mental health care for DC's diverse community. Specializing in trauma, addiction, and youth services – because everyone deserves expert care.</p>
    <div style="font-size:12.5px;color:var(--blue);margin:20px 0 4px 4px">What Makes Us Different:</div>
    <ul class="ticks" style="margin-left:4px"><li>Same-week appointments</li><li>Sliding scale fees</li><li>99% client success rate</li></ul>
    <p style="margin-top:16px">Noren Health provides expert trauma, addiction &amp; youth mental health care in DC. Same-week appointments. Sliding scale fees.</p>
  </div>
  <span class="btn btn-primary" style="left:653px;top:407px;width:160px;height:36px">Start Healing Today</span>
</section>

<section class="values">
  <h2 class="section-title serif" style="left:0;right:0;text-align:center;top:32px">Our Core Value</h2>
  <div class="value" style="left:194px">Compassionate &amp;<br>Unbiased</div>
  <div class="value" style="left:430px">Evidence-Based &amp;<br>Holistic</div>
  <div class="value" style="left:666px">Safe &amp;<br>Serene Spaces</div>
  <div class="value" style="left:902px">Always<br>Evolving</div>
  <div class="value-icon" style="left:263px"><i role="img" aria-label="Compassion icon"></i></div>
  <div class="value-icon" style="left:499px"><i role="img" aria-label="Holistic care icon"></i></div>
  <div class="value-icon" style="left:735px"><i role="img" aria-label="Safe spaces icon"></i></div>
  <div class="value-icon" style="left:971px"><i role="img" aria-label="Growth icon"></i></div>
</section>

<section class="support">
  <span class="plus" style="left:1090px;top:36px"></span>
  <span class="plus" style="left:28px;top:403px"></span>
  <div class="photo" role="img" aria-label="Photo of the support team standing together" style="left:137px;top:64px;width:463px;height:356px;border-radius:8px;background:linear-gradient(135deg,#cfc7bc,#8c7b6c 45%,#3f4a58)"></div>
  <div class="abs trust">
    <svg width="30" height="30" viewBox="0 0 24 24" fill="none" stroke="#fff" stroke-width="1.5"><path d="M12 20s-7-4.5-7-10a4 4 0 0 1 7-2.5A4 4 0 0 1 19 10c0 5.5-7 10-7 10z"/></svg>
    Trust Us With<br>All Your Heart
  </div>
  <div class="abs" style="left:683px;top:79px;width:420px">
    <div class="eyebrow">Your Support Team</div>
    <h2 class="serif" style="font-size:28px;line-height:34px;margin:12px 0 12px">Immediate Help<br>When You Need It Most</h2>
    <p style="font-size:12px;line-height:21px;color:var(--body)">Noren Health provides 24/7 crisis support for individuals and families facing mental health or addiction challenges. Our licensed professionals offer:</p>
    <ul class="ticks" style="margin-top:18px"><li>Emergency mental health triage</li><li>Same-day crisis appointments</li><li>Safety planning &amp; stabilization</li></ul>
    <p style="font-size:13px;margin-top:20px">In a crisis? Don't hesitate – we're here to listen and help.</p>
    <p style="font-size:13px;margin-top:12px;font-weight:500;display:flex;align-items:center;gap:8px">Call Now:
      <svg width="16" height="16" viewBox="0 0 24 24" fill="none" stroke="#2e86cf" stroke-width="2"><path d="M5 3h4l2 5-3 2a11 11 0 0 0 6 6l2-3 5 2v4a2 2 0 0 1-2 2A18 18 0 0 1 3 5a2 2 0 0 1 2-2z"/></svg>
      <span style="color:var(--blue);font-weight:400">(555) 014-2287</span> (24 hours, 7 days a week)</p>
  </div>
</section>

<section class="facilities">
  <h2 class="section-title serif" style="left:137px;top:78px">Our Treatment Facilities</h2>
  <p class="section-sub" style="left:137px;top:124px">Comprehensive care environments designed for healing and growth</p>
  <span class="btn btn-ghost" style="left:943px;top:91px;width:141px;height:40px">View All Facilities</span>
  <div class="facility" style="left:137px"><div class="ico"><i></i></div><h3>Medical &amp; Clinical Care</h3><ul><li>24/7 psychiatric nursing staff</li><li>Medication management suites</li><li>Detox observation rooms</li></ul></div>
  <div class="facility" style="left:378px"><div class="ico"><i></i></div><h3>Therapeutic Spaces</h3><ul><li>Group therapy circles</li><li>Private counseling rooms</li><li>Family intervention suites</li></ul></div>
  <div class="facility" style="left:619px"><div class="ico"><i></i></div><h3>Holistic Wellness Areas</h3><ul><li>Yoga/movement studios</li><li>Sensory relaxation pods</li><li>Outdoor meditation gardens</li></ul></div>
  <div class="facility" style="left:860px"><div class="ico"><i></i></div><h3>Safety-Enhanced Units</h3><ul><li>Crisis stabilization rooms</li><li>Secure outdoor spaces</li><li>Emergency response-trained staffoons</li></ul></div>
</section>

<section class="insights">
  <h2 class="section-title serif" style="left:0;right:0;text-align:center;top:28px">Latest Mental Health Insights</h2>
  <p class="section-sub" style="left:0;right:0;text-align:center;top:78px">Evidence-based guidance from our care team</p>
  <article class="post" style="left:157px">
    <div class="thumb" role="img" aria-label="Photo of a counseling session" style="background:linear-gradient(135deg,#d9d6d0,#8f8f94 60%,#5c6470)"></div>
    <div class="date">July 7, 2024</div>
    <h3>Identifying Fraudulent Rehab Centers</h3>
    <ul><li>No licensed staff on site</li><li>Pressure to sign insurance forms</li><li>"Guaranteed cure" promises</li></ul>
    <a>Read more</a>
  </article>
  <article class="post" style="left:474px">
    <div class="thumb" role="img" aria-label="Photo of medication and a notebook on a wooden table" style="background:linear-gradient(135deg,#5a4030,#8b6a4f 50%,#4b3a2e)"></div>
    <div class="date">September 8, 2022</div>
    <h3>Opioid Crisis Update: Palm Beach County</h3>
    <ul><li>421 deaths (12% increase from 2021)</li><li>Fentanyl involved in 89% of cases</li><li>New naloxone access points mapped</li></ul>
    <a class="muted">Read more</a>
  </article>
  <article class="post" style="left:791px">
    <div class="thumb" role="img" aria-label="Photo of a group therapy circle" style="background:linear-gradient(135deg,#9b5b45,#c9a58a 50%,#6a5247)"></div>
    <div class="date">August 1, 2024</div>
    <h3>2023's Top Rehab Facilities</h3>
    <ol><li>Linden Hollow (Trauma-focused)</li><li>Stillwater Point (LGBTQ+ specialty)</li><li>Noren Health (Sliding scale option)</li></ol>
    <a class="muted">Read more</a>
  </article>
</section>

<footer class="site-footer">
  <div class="brand" style="left:170px;top:92px">
    <span class="brand-name">Noren Health Services</span>
  </div>
  <p class="abs f-tag">Compassionate care for Washington DC's<br>mental health needs</p>
  <div class="f-col" style="left:474px"><h4>QUICK LINKS</h4><ul><li>Our Services</li><li>Crisis Support</li><li>Meet the Team</li><li>Patient Portal</li><li>Success Stories</li></ul></div>
  <div class="f-col" style="left:645px"><h4>For Providers</h4><ul><li>Careers</li><li>Refer a Patient</li><li>Provider Login</li></ul></div>
  <div class="f-col" style="left:881px"><h4>CONTACT INFO</h4>
    <div class="contact-row"><span class="contact-dot"><svg width="14" height="14" viewBox="0 0 24 24" fill="none" stroke="#fff" stroke-width="2"><path d="M5 3h4l2 5-3 2a11 11 0 0 0 6 6l2-3 5 2v4a2 2 0 0 1-2 2A18 18 0 0 1 3 5a2 2 0 0 1 2-2z"/></svg></span>+1 555 014 2287</div>
    <div class="contact-row"><span class="contact-dot"><svg width="14" height="14" viewBox="0 0 24 24" fill="none" stroke="#fff" stroke-width="2"><rect x="3" y="5" width="18" height="14" rx="2"/><path d="M3 7l9 6 9-6"/></svg></span>info@norenhealth.com</div>
    <div class="contact-row"><span class="contact-dot"><svg width="14" height="14" viewBox="0 0 24 24" fill="none" stroke="#fff" stroke-width="2"><path d="M12 21s-7-6-7-11a7 7 0 0 1 14 0c0 5-7 11-7 11z"/><circle cx="12" cy="10" r="2.5"/></svg></span>Washington DC</div>
  </div>
  <div class="abs footer-rule"></div>
  <p class="abs copyright">© 2024 Noren Health Services. All rights reserved.</p>
</footer>

</body>
</html>
```